Updated DJ business Card showing other businesses

DJ Kestro offers professional mobile dj services including DJ. MC. Karaoke.
Silent Disco (will attach logo)
I also offer a 360 Photo Booth.

Contact info:
(555) 013-4472
marcus.tellgren@lumomail.net
Social Media @DJKestroNWX

```html
<!DOCTYPE html>
<html lang="en">
<head>
<meta charset="utf-8">
<title>DJ Kestro Business Card</title>
<link href="https://fonts.googleapis.com/css2?family=Barlow+Semi+Condensed:wght@500;600;700;800&display=swap" rel="stylesheet">
<style>
  :root {
    --backdrop: #2a2a2c;
    --card: #0b0b0c;
    --card-sheen: #1e1e20;
    --ink: #ffffff;
    --accent: #d81f4a;
    --muted: #cfcfd2;
  }
  html, body {
    margin: 0;
    width: 1200px;
    height: 900px;
    overflow: hidden;
    background: var(--backdrop);
    font-family: "Barlow Semi Condensed", sans-serif;
    color: var(--ink);
  }
  .sheet {
    width: 1200px;
    height: 900px;
    display: flex;
    flex-direction: column;
    align-items: center;
    justify-content: center;
    gap: 40px;
  }
  .card {
    position: relative;
    width: 700px;
    height: 400px;
    border-radius: 22px;
    background: linear-gradient(105deg, var(--card) 0%, var(--card) 48%, var(--card-sheen) 58%, var(--card) 70%, var(--card) 100%);
    box-shadow: 0 14px 30px rgba(0,0,0,.55);
    overflow: hidden;
    box-sizing: border-box;
    padding: 0 60px;
  }
  .wordmark {
    display: flex;
    align-items: center;
    gap: 18px;
    font-weight: 800;
    font-size: 104px;
    line-height: 1;
    letter-spacing: 1px;
    color: var(--ink);
  }
  .wordmark-dot {
    width: 34px;
    height: 34px;
    border-radius: 50%;
    background: var(--accent);
    flex: none;
  }
  .card-front .wordmark { margin-top: 62px; }
  .tagline {
    margin: 22px 0 4px;
    font-weight: 600;
    font-size: 21px;
    letter-spacing: 1px;
    text-transform: uppercase;
  }
  .services {
    display: flex;
    align-items: center;
    gap: 14px;
    font-weight: 700;
    font-size: 48px;
    line-height: 1.1;
    text-transform: uppercase;
  }
  .services .divider {
    width: 3px;
    height: 40px;
    background: var(--ink);
  }
  .partner {
    display: flex;
    align-items: center;
    gap: 8px;
    font-weight: 700;
    font-size: 26px;
  }
  .partner-dot {
    width: 18px;
    height: 18px;
    border-radius: 50%;
    border: 2px solid var(--ink);
    box-sizing: border-box;
  }
  .addon {
    margin-top: 6px;
    font-weight: 600;
    font-size: 16px;
    letter-spacing: 1px;
    text-transform: uppercase;
    color: var(--muted);
  }
  .card-back .wordmark { margin-top: 56px; }
  .contact { margin-top: 26px; text-transform: uppercase; }
  .contact-phone {
    font-weight: 700;
    font-size: 50px;
    line-height: 1.05;
  }
  .contact-email {
    font-weight: 600;
    font-size: 28px;
    letter-spacing: 1px;
    margin-top: 4px;
  }
  .contact-social {
    display: flex;
    align-items: center;
    gap: 8px;
    margin-top: 6px;
    font-weight: 600;
    font-size: 22px;
    letter-spacing: 1px;
  }
  .contact-social .at-mark {
    width: 16px;
    height: 16px;
    border-radius: 3px;
    border: 2px solid var(--ink);
    box-sizing: border-box;
  }
</style>
</head>
<body>
<main class="sheet">
  <section class="card card-front">
    <div class="wordmark"><span>DJ KESTRO</span><span class="wordmark-dot"></span></div>
    <p class="tagline">DJ Kestro offers professional mobile DJ services</p>
    <div class="services">
      <span>DJ</span><span class="divider"></span>
      <span>MC</span><span class="divider"></span>
      <span>Karaoke</span><span class="divider"></span>
      <span class="partner"><span class="partner-dot"></span>Hushwave</span>
    </div>
    <p class="addon">I also offer a 360 photo booth.</p>
  </section>

  <section class="card card-back">
    <div class="wordmark"><span>DJ KESTRO</span><span class="wordmark-dot"></span></div>
    <div class="contact">
      <div class="contact-phone">(555) 013-4472</div>
      <div class="contact-email">marcus.tellgren@lumomail.net</div>
      <div class="contact-social"><span class="at-mark"></span>@DJKestroNWX</div>
    </div>
  </section>
</main>
</body>
</html>
```